Flyer Design Project for Brightwater Wellbeing Rooms

We are a psychology clinic that specialises in eating, parenting and chronic illness & pain. See our website for a summary.

We need a flyer that will go to doctors and schools in the local area.

Things to include on the front page:

Immediate appointments available
After hours appointments available
Male and female psychologists

Phone 9563 2190
Web brightwaterwellbeingrooms.com.au

On the back page:

Phone 9563 2190
Suite 1/1287 Marlowe Rd, Kelverton East 3185.
brightwaterwellbeingrooms.com.au

Parenting: Parenthood is an amazing journey, but for lots of people it raises all sorts of issues from fear of birth, breastfeeding difficulties and settling problems, to toddler discipline and food fussiness all the way through to getting help for your depressed or anxious adolescent. Our Parenting Psychologists can help you be the best parent you can be which will in turn lead to happier families, homes, children and parents.

Chronic illness/pain: Diabetes, heart disease, arthritis, asthma, migraines, dizziness, chronic fatigue syndrome, infertility, and PCOS are just some of the conditions that can be managed with psychological interventions. Everything we do is about helping you to manage your condition and get back to focusing on what you really want your life to be about.

Eating: Whether you suffer from anorexia, bulimia or binge eating, our strategies help you develop a healthy relationship with food and your body. The practical tips and strategies that we can provide are very useful for people undergoing lapband surgery or liposuction.

I am interested in whether the photographs that I have already purchased can be used...so please have a look through the website and see which you think will suit your design. Photographs are not absolutely necessary though, so if it doesn't fit with your idea that is okay too.
Updates

HI Everyone,

Thanks for submitting so far! I haven't found anything yet that has hit the mark. And I am thinking that is my fault and maybe that way i have described what I want. I apologise and hope that this update might help.

This brochure is likely to sit with lots of other brochures in a doctors waiting room so it needs to be different - so that it will be noticed.

The majority of our market are women - so something feminine is important. Maybe it needs to be a little more playful that I had initially thought. Like maybe not your standard blocky text and bolds and primary colours. But something more creative, more personal.

I want to not focus just on the family theme. Parenting is one area that we cover, but also we help people with eating disorders and chronic illness/chronic pain. So the photographs that I use need to be more general. It is importnat to focus on happy and healthy looking people. As we went to appeal to what my potential clients want to look like and feel like.

I do hope this helps to guide you. I promise that once I see a flyer that I could choose, I will turn the funding to guaranteed. I did this last time...I am just a bit nervous as I haven't received anything yet that I am excited about.

Kindest regards,

Marnie.

Hi Everyone,

Thank you for your designs coming in! As promised, as soon as I received a design that I could see myself choosing I would change the status from refundable to committed. I have now done this!

I have received a design that I would say is good. It is not perfect however...so please keep the ideas coming.

To give more direction, the one that came in has a nice theme that runs through the brochure. Not too many different types of font and colours detracting from the flow of the flyer. However, the thing that I am concerned about is whether it will stand out enough on a rack of other flyers in a doctors waiting room.

I hope this helps with your creative ideas.

Thanks again to everyone!

Marnie.

Thanks SO much to everyone who is putting in designs. You are making my decision difficult!

I am wondering if you can update your designs with a few things:

can I ask you to make some text changes:

1. Can we have a heading on the front page: Psychologists  and then can you put Kelverton East in smaller writing just below it?

2. Id like to say on the front: Specialising in parenting, disordered eating and chronic pain & illness

3. Delete Male & Female Psychologists

4. In general we dont' need to have the logo standing out. We don't have a well known brand yet, so I am not wanting to take up valuable space with this - so perhaps it shoudl be small and maybe just on the back? Keeping the name of our clinic on the front with the website shoudl be sufficient.

Thanks heaps everyone...I will make decision very soon!

Target Market(s)

20-40 year olds. Working. Educated. Female. They might have a family/children.
Australian. Engish speaking.

Industry/Entity Type

Clinic

Requirements
Must have
• I would like to include our logo. Please do not use the colour green that it is in. I hate that colour! but I LOVE the logo.

I would like to follow through with some of the themes of the website and other stationary.

I will attach some of the other stationary I have had designed.

I really like the colours in the letterhead - especially that blue of the logo.

I think it needs to have a dash of colour with it at least...something that will stand out and be noticed on a brochure rack...but also have a look of class/sophistication/modern.
Nice to have
• Perhaps photograph of happy and healthy people.
Should not have
• I don't like bold text or too many different types of fonts.

It shouldn't look too cluttered so I might need to reduce the text I have included - I will need to see it first.

```html
<!DOCTYPE html>
<html lang="en">
<head>
<meta charset="utf-8">
<title>Brightwater Wellbeing Rooms – Flyer</title>
<link rel="stylesheet" href="https://fonts.googleapis.com/css2?family=Open+Sans:wght@400;600;700&display=swap">
<style>
  :root {
    --slate: #4f7c92;
    --teal: #62b7b9;
    --teal-deep: #4c9c9f;
    --charcoal: #4a5459;
    --ink-brand: #3e5c69;
    --ink-body: #5b2c26;
    --ink-list: #1f1f1f;
    --phone-red: #6a1d12;
    --band-brown: #7b6b5f;
    --band-brown-dark: #685a4f;
    --tick: #5c9b2f;
    --page: #ffffff;
    --canvas: #ffffff;
    --phone-blue: #3d6f8a;
  }
  * { box-sizing: border-box; margin: 0; padding: 0; }
  html, body { width: 1200px; height: 900px; overflow: hidden; background: var(--canvas); }
  body { position: relative; font-family: "Open Sans", Arial, sans-serif; }

  .page {
    position: absolute; top: 72px; width: 480px; height: 702px;
    background: var(--page); overflow: hidden;
    box-shadow: 0 2px 10px rgba(0,0,0,0.28);
  }
  .page--front { left: 78px; }
  .page--back { left: 626px; }

  /* colour stripe bars */
  .stripe-bar { position: absolute; left: 0; display: flex; width: 100%; }
  .stripe-bar span { flex: 1; }
  .stripe-bar .s1 { background: var(--slate); }
  .stripe-bar .s2 { background: var(--teal); }
  .stripe-bar .s3 { background: var(--teal-deep); }
  .stripe-bar .s4 { background: var(--charcoal); }
  .stripe-bar--bottom { bottom: 0; height: 26px; }
  .stripe-bar--top { top: 0; height: 21px; }

  .header-blocks { position: absolute; top: 0; left: 244px; width: 236px; height: 100px; display: flex; }
  .header-blocks span { flex: 1; }
  .header-blocks .s1 { background: var(--slate); }
  .header-blocks .s2 { background: var(--teal); }
  .header-blocks .s3 { background: var(--teal-deep); flex: 1.15; }

  /* brand name lockup */
  .brand { position: absolute; display: flex; align-items: center; gap: 12px; }
  .brand__dot { width: 54px; height: 54px; border-radius: 50%; background: var(--teal); flex: none; }
  .brand__name {
    font-weight: 400; color: var(--ink-brand); text-transform: uppercase;
    letter-spacing: 3px; font-size: 15px; line-height: 19px;
  }
  .page--front .brand { left: 14px; top: 26px; }
  .page--back .brand { left: 40px; top: 96px; }
  .page--back .brand__dot { width: 46px; height: 46px; }
  .page--back .brand__name { font-size: 12px; line-height: 15px; letter-spacing: 2.4px; }

  /* photo areas */
  .photo-front {
    position: absolute; left: 0; top: 105px; width: 480px; height: 320px;
    background: linear-gradient(120deg, #d9e9c9 0%, #f2d9c4 35%, #e8c3a4 55%, #cfd9d3 80%, #e4ecef 100%);
  }
  .photo-front__wave { position: absolute; left: 0; top: 330px; width: 480px; height: 100px; }
  .photo-back {
    position: absolute; left: 215px; top: 38px; width: 232px; height: 175px;
    background: linear-gradient(90deg, #f7f2ee 0%, #e9c1b0 30%, #f4e3c8 55%, #eecfd9 80%, #f7f2ee 100%);
  }

  /* checklist */
  .checklist { position: absolute; left: 38px; top: 438px; list-style: none; }
  .checklist li {
    display: flex; align-items: center; gap: 14px; height: 37px;
    font-size: 21px; color: var(--ink-list); font-weight: 400;
  }
  .checklist svg { width: 34px; height: 30px; flex: none; }

  /* torn contact band */
  .contact-band { position: absolute; left: 34px; top: 548px; width: 422px; height: 102px; }
  .contact-band svg.band-shape { position: absolute; inset: 0; width: 100%; height: 100%; }
  .contact-band__phone {
    position: absolute; left: 0; right: 30px; top: 18px; text-align: center;
    font-weight: 700; font-size: 27px; color: var(--phone-red);
    display: flex; justify-content: center; align-items: center; gap: 6px;
  }
  .contact-band__phone svg { width: 26px; height: 26px; }
  .contact-band__web {
    position: absolute; left: 0; right: 30px; top: 58px; text-align: center;
    font-weight: 700; font-size: 16px; color: #ffffff;
  }

  /* back copy */
  .services { position: absolute; left: 30px; top: 200px; width: 420px; }
  .services p {
    font-size: 11.6px; line-height: 16.6px; color: var(--ink-body);
    text-align: justify; margin-bottom: 15px;
  }
  .services p:nth-child(3) { margin-top: 10px; }

  .back-contact { position: absolute; left: 0; top: 552px; width: 100%; text-align: center; }
  .back-contact__phone {
    display: flex; justify-content: center; align-items: center; gap: 8px;
    font-weight: 700; font-size: 22px; color: var(--phone-blue); margin-left: -8px;
  }
  .back-contact__phone svg { width: 40px; height: 40px; }
  .back-contact__address { margin-top: 10px; font-size: 15.5px; color: #2a2a2a; }
  .back-contact__web { margin-top: 4px; font-size: 15.5px; color: #2a2a2a; }
</style>
</head>
<body>

<section class="page page--front" aria-label="Flyer front page">
  <div class="header-blocks"><span class="s1"></span><span class="s2"></span><span class="s3"></span></div>
  <div class="brand">
    <span class="brand__dot"></span>
    <span class="brand__name">Brightwater<br>Wellbeing<br>Rooms</span>
  </div>

  <div class="photo-front" role="img" aria-label="Photograph of a smiling family of four playing together outdoors"></div>
  <svg class="photo-front__wave" viewBox="0 0 480 100" preserveAspectRatio="none" aria-hidden="true">
    <path d="M0 62 C120 30 300 0 480 12 L480 100 L0 100 Z" fill="#ffffff"/>
    <path d="M0 62 C120 30 300 0 480 12 L480 30 C300 18 130 42 0 70 Z" fill="#4c9c9f"/>
  </svg>

  <ul class="checklist">
    <li><svg viewBox="0 0 34 30"><rect x="2" y="10" width="18" height="18" fill="none" stroke="#7a8a88" stroke-width="1.5"/><path d="M6 16 L12 23 L31 3" fill="none" stroke="var(--tick)" stroke-width="4" stroke-linecap="round" stroke-linejoin="round"/></svg>Immediate appointments available</li>
    <li><svg viewBox="0 0 34 30"><rect x="2" y="10" width="18" height="18" fill="none" stroke="#7a8a88" stroke-width="1.5"/><path d="M6 16 L12 23 L31 3" fill="none" stroke="var(--tick)" stroke-width="4" stroke-linecap="round" stroke-linejoin="round"/></svg>After hours appointments available</li>
    <li><svg viewBox="0 0 34 30"><rect x="2" y="10" width="18" height="18" fill="none" stroke="#7a8a88" stroke-width="1.5"/><path d="M6 16 L12 23 L31 3" fill="none" stroke="var(--tick)" stroke-width="4" stroke-linecap="round" stroke-linejoin="round"/></svg>Male and female psychologists</li>
  </ul>

  <div class="contact-band">
    <svg class="band-shape" viewBox="0 0 422 102" preserveAspectRatio="none" aria-hidden="true">
      <path d="M4 6 L60 3 L120 7 L190 2 L260 6 L330 3 L395 6 L395 96 L330 99 L250 95 L170 100 L90 96 L20 99 L2 96 L6 50 Z" fill="var(--band-brown)"/>
      <path d="M395 6 L412 14 L416 72 C410 86 400 94 392 98 L395 6 Z" fill="#f3f1ee"/>
      <path d="M392 98 C404 80 410 60 395 40 L395 98 Z" fill="#d9d4ce"/>
    </svg>
    <div class="contact-band__phone">
      <svg viewBox="0 0 26 26" aria-hidden="true"><circle cx="13" cy="13" r="11.5" fill="none" stroke="var(--phone-red)" stroke-width="2"/><path d="M9 7 C7 9 7 12 9 15 C11 18 14 20 17 19 L18 17 L15.5 15 L14 16 C12.5 15 11 13.5 10.5 12 L11.5 10.5 L10 7.5 Z" fill="var(--phone-red)"/></svg>
      9563 2190
    </div>
    <div class="contact-band__web">www.brightwaterwellbeingrooms.com.au</div>
  </div>

  <div class="stripe-bar stripe-bar--bottom"><span class="s1"></span><span class="s2"></span><span class="s3"></span><span class="s4"></span><span class="s2"></span></div>
</section>

<section class="page page--back" aria-label="Flyer back page">
  <div class="stripe-bar stripe-bar--top"><span class="s1"></span><span class="s2"></span><span class="s3"></span><span class="s4"></span><span class="s2"></span></div>

  <div class="brand">
    <span class="brand__dot"></span>
    <span class="brand__name">Brightwater<br>Wellbeing<br>Rooms</span>
  </div>
  <div class="photo-back" role="img" aria-label="Photograph of three cheerful children holding fruit slices in front of their eyes"></div>

  <div class="services">
    <p>Parenting: Parenthood is an amazing journey, but for lots of people it raises all sorts of issues from fear of birth, breastfeeding difficulties and settling problems, to toddler discipline and food fussiness all the way through to getting help for your depressed or anxious adolescent. Our Parenting Psychologists can help you be the best parent you can be which will in turn lead to happier families, homes, children and parents.</p>
    <p>Chronic illness/pain: Diabetes, heart disease, arthritis, asthma, migraines, dizziness, chronic fatigue syndrome, infertility, and PCOS are just some of the conditions that can be managed with psychological interventions. Everything we do is about helping you to manage your condition and get back to focusing on what you really want your life to be about.</p>
    <p>Eating: Whether you suffer from anorexia, bulimia or binge eating, our strategies help you develop a healthy relationship with food and your body. The practical tips and strategies that we can provide are very useful for people undergoing lapband surgery or liposuction.</p>
  </div>

  <div class="back-contact">
    <div class="back-contact__phone">
      <svg viewBox="0 0 40 40" aria-hidden="true"><circle cx="20" cy="20" r="17" fill="none" stroke="var(--teal)" stroke-width="2.5"/><path d="M14 10 C11 13 11 18 14 23 C17 28 22 31 26 29 L27.5 26 L24 23 L22 24.5 C19.5 23 17.5 20.5 16.5 18 L18 16 L16 11 Z" fill="var(--teal)"/></svg>
      9563 2190
    </div>
    <div class="back-contact__address">Suite 1/1287 Marlowe Rd, Kelverton East 3185.</div>
    <div class="back-contact__web">brightwaterwellbeingrooms.com.au</div>
  </div>

  <div class="stripe-bar stripe-bar--bottom"><span class="s1"></span><span class="s2"></span><span class="s3"></span><span class="s4"></span><span class="s2"></span></div>
</section>

</body>
</html>
```